North Fern Holdings Business Card

A business card design to accompany the logo design you completed on Artisan Hive. We are open to your proposals. I did add one idea below that might work, but we aren't married to the idea. The company is a real estate services company. Clientele are typically high net worth individuals, executive level employment or owners of their own company, 30-60 years old.

Our 1 (bad?) idea: double sided card; One side landscape with logo and word mark. Other side Portrait with the logo only (oversize watermark maybe?). Somewhere add text of Name (Marcus Pellington), Title (Principal), phone # (949-555-0173) and email address (marcus@northfernhq.com). There would be a second design with my wife's name, number and email in place of mine.

Again totally open to ideas here.

Industry/Entity Type

Real Estate

```html
<!DOCTYPE html>
<html lang="en">
<head>
<meta charset="utf-8">
<title>North Fern Holdings Business Card</title>
<link href="https://fonts.googleapis.com/css2?family=Cinzel:wght@400&display=swap" rel="stylesheet">
<style>
  :root {
    --canvas: #ffffff;
    --card: #ffffff;
    --brand-green: #5b9548;
    --ink-grey: #5f5f5f;
    --card-shadow: rgba(0, 0, 0, 0.35);
  }
  * { box-sizing: border-box; margin: 0; padding: 0; }
  html, body {
    width: 1028px;
    height: 1200px;
    overflow: hidden;
    background: var(--canvas);
  }
  .canvas {
    position: relative;
    width: 1028px;
    height: 1200px;
    font-family: "Cinzel", "Times New Roman", serif;
  }
  .card {
    position: absolute;
    background: var(--card);
    box-shadow: 4px 6px 12px var(--card-shadow);
  }

  /* Portrait: details side */
  .card--portrait {
    left: 155px;
    top: 417px;
    width: 208px;
    height: 366px;
    text-align: center;
  }
  .brand-lockup {
    position: absolute;
    display: flex;
    align-items: center;
  }
  .card--portrait .brand-lockup {
    left: 20px;
    top: 50px;
    gap: 10px;
  }
  .brand-mark {
    flex: none;
    border-radius: 50%;
    background: var(--brand-green);
  }
  .card--portrait .brand-mark { width: 26px; height: 26px; }
  .brand-name {
    color: var(--brand-green);
    font-weight: 400;
    text-align: left;
    line-height: 1.05;
  }
  .card--portrait .brand-name { font-size: 15px; }
  .holder {
    position: absolute;
    left: 0;
    right: 0;
    top: 176px;
  }
  .holder-name {
    color: var(--ink-grey);
    font-size: 15px;
    letter-spacing: 0.2px;
  }
  .holder-title {
    color: var(--brand-green);
    font-size: 12px;
    margin-top: 3px;
  }
  .contact {
    position: absolute;
    left: 0;
    right: 0;
    top: 309px;
    color: var(--ink-grey);
    font-size: 11.5px;
    line-height: 16px;
  }
  .contact .at { color: var(--brand-green); }
  .accent-band {
    position: absolute;
    left: 0;
    right: 0;
    bottom: 0;
    height: 19px;
    background: var(--brand-green);
  }

  /* Landscape: brand side */
  .card--landscape {
    left: 514px;
    top: 497px;
    width: 362px;
    height: 206px;
  }
  .card--landscape .brand-lockup {
    left: 38px;
    top: 64px;
    gap: 22px;
  }
  .card--landscape .brand-mark { width: 54px; height: 54px; }
  .card--landscape .brand-name { font-size: 30px; }
</style>
</head>
<body>
<main class="canvas">

  <section class="card card--portrait" aria-label="Business card, details side">
    <div class="brand-lockup">
      <span class="brand-mark" aria-hidden="true"></span>
      <div class="brand-name">North Fern<br>Holdings</div>
    </div>
    <div class="holder">
      <p class="holder-name">Marcus Pellington</p>
      <p class="holder-title">Principal</p>
    </div>
    <div class="contact">
      <p class="contact-phone">949-555-0173</p>
      <p class="contact-email">marcus<span class="at">@northfernhq</span>.com</p>
    </div>
    <div class="accent-band"></div>
  </section>

  <section class="card card--landscape" aria-label="Business card, brand side">
    <div class="brand-lockup">
      <span class="brand-mark" aria-hidden="true"></span>
      <div class="brand-name">North Fern<br>Holdings</div>
    </div>
  </section>

</main>
</body>
</html>
```